Help a start up law firm make an impression! - Website

We are a property development and conveyancing law firm looking for some to design our website. The initial brief is for 6 pages with scope for on-going work.

Law firms are traditionally quite conservative and we want to break the mold. We want to come across as fun and modern, while still being professional.

A good example is https://quorrantlaw.com.au/. It's professional yet modern.
Updates

Another good site I like in the same industry: https://www.tindalemarshconveyancing.com.au/

Target Market(s)

Tech savy home buyers and sellers - generally 30 to 50 years old

Industry/Entity Type

Law Firm

Coding

Coded - Design and coding required

Number of Pages Required

5+ page

Font styles to use
Other font styles liked:
• No idea

Colors
f04a50

Requirements
Must have
• The elements set out in the design brief document

```html
<!DOCTYPE html>
<html lang="en">
<head>
<meta charset="utf-8">
<title>Hartwell Law – The Property Law Experts</title>
<link rel="stylesheet" href="https://fonts.googleapis.com/css2?family=Montserrat:wght@400;700&family=Open+Sans:wght@400&display=swap">
<style>
  :root {
    --brand-red: #d8455a;
    --ink: #1a1a1a;
    --nav-ink: #333333;
    --white: #ffffff;
    --caption-bg: rgba(112, 102, 104, 0.72);
    --hero-top: #6b625f;
    --hero-mid: #8a7672;
    --hero-low: #3b302d;
    --hero-glow: #c98f7e;
  }
  * { box-sizing: border-box; margin: 0; padding: 0; }
  html, body {
    width: 1200px;
    height: 605px;
    overflow: hidden;
    background: var(--white);
  }
  .site {
    position: relative;
    width: 1200px;
    height: 605px;
  }
  .site-header {
    position: relative;
    height: 78px;
    background: var(--white);
  }
  .brand {
    position: absolute;
    left: 52px;
    top: 24px;
    display: flex;
    align-items: center;
    gap: 8px;
    font-family: "Montserrat", sans-serif;
    font-weight: 700;
    font-size: 25px;
    color: var(--ink);
    letter-spacing: -0.3px;
  }
  .brand-mark {
    width: 10px;
    height: 10px;
    background: var(--brand-red);
  }
  .main-nav {
    position: absolute;
    top: 0;
    left: 0;
    width: 100%;
    height: 78px;
    font-family: "Open Sans", sans-serif;
    font-size: 13.5px;
    color: var(--nav-ink);
  }
  .nav-link {
    position: absolute;
    top: 31px;
    white-space: nowrap;
  }
  .nav-link.is-active { color: var(--brand-red); }
  .nav-link.is-active::before {
    content: "";
    position: absolute;
    top: -31px;
    left: -20px;
    right: -20px;
    height: 3px;
    background: var(--brand-red);
  }
  .nav-search {
    position: absolute;
    left: 1119px;
    top: 34px;
  }
  .hero {
    position: relative;
    height: 527px;
    overflow: hidden;
  }
  .hero-photo {
    position: absolute;
    inset: 0;
    background:
      radial-gradient(ellipse at 85% 20%, rgba(201,143,126,0.35), transparent 55%),
      linear-gradient(180deg, var(--hero-top) 0%, var(--hero-mid) 42%, var(--hero-glow) 62%, var(--hero-low) 82%, #2a2220 100%);
  }
  .hero-title {
    position: absolute;
    left: 172px;
    top: 168px;
    width: 840px;
    height: 76px;
    background: var(--caption-bg);
    font-family: "Montserrat", sans-serif;
    font-weight: 400;
    font-size: 51px;
    line-height: 76px;
    color: var(--white);
    text-align: center;
    letter-spacing: 0.5px;
  }
  .hero-tagline {
    position: absolute;
    left: 168px;
    top: 258px;
    width: 847px;
    height: 38px;
    background: var(--caption-bg);
    font-family: "Montserrat", sans-serif;
    font-weight: 400;
    font-size: 20px;
    line-height: 38px;
    color: var(--white);
    text-align: center;
  }
  .hero-cta {
    position: absolute;
    left: 0;
    width: 100%;
    top: 344px;
    text-align: center;
    font-family: "Montserrat", sans-serif;
    font-size: 11px;
    letter-spacing: 0.5px;
    color: #2e2626;
  }
</style>
</head>
<body>
<div class="site">
  <header class="site-header">
    <div class="brand"><span class="brand-name">Hartwell Law</span><span class="brand-mark"></span></div>
    <nav class="main-nav">
      <span class="nav-link is-active" style="left:408px">Home</span>
      <span class="nav-link" style="left:487px">Who We Are</span>
      <span class="nav-link" style="left:606px">What We Do</span>
      <span class="nav-link" style="left:724px">Where We Work</span>
      <span class="nav-link" style="left:867px">Careers</span>
      <span class="nav-link" style="left:956px">News</span>
      <span class="nav-link" style="left:1031px">Contact</span>
      <svg class="nav-search" width="13" height="13" viewBox="0 0 13 13" aria-label="Search">
        <circle cx="5.2" cy="5.2" r="4" fill="none" stroke="#333" stroke-width="2"/>
        <line x1="8.2" y1="8.2" x2="12" y2="12" stroke="#333" stroke-width="2.2" stroke-linecap="round"/>
      </svg>
    </nav>
  </header>
  <section class="hero">
    <div class="hero-photo" role="img" aria-label="Sepia-toned photo of a city skyline at dusk with a lit steel bridge over a river"></div>
    <h1 class="hero-title">THE PROPERTY LAW EXPERTS</h1>
    <p class="hero-tagline">Unrivaled response times, fixed fee options and experienced property lawyers</p>
    <span class="hero-cta">CONTACT US</span>
  </section>
</div>
</body>
</html>
```